Medical IT Business with New logo needs a fresh stationary design

First time on pixel Harbor; Thought I would give it a go.
This project is for business cards alone but we have loads of design work that needs to take place in the immediate future.

We provide IT services to the Medical Industry and value ourselves as offering a premium product to the market.

I am after a fresh, clean design using full colour 2 sided cards which includes our current colour palettes from our logo.

Card's must include:
- Logo
- Slogan
- Name
- Adress
- Email
- Phone
- Fax
- Mobile

Target Market(s)

Surgeons, High Profile Medical Personnel

Industry/Entity Type

Business

Fonts, CMYK Colours and Logo files attached.

Requirements
Must have
• Card's must include:
• - Logo
• - Slogan
• - Name
• - Adress
• - Email
• - Phone
• - Fax
• - Mobile
Nice to have
• Needs to incorporate our colour palette (attached CMYK colours)
Should not have
• Black backgrounds. Black text ok.

```html
<!DOCTYPE html>
<html lang="en">
<head>
<meta charset="utf-8">
<title>Clearpath Clinical – Business Cards</title>
<link href="https://fonts.googleapis.com/css2?family=Open+Sans:wght@400;600;700&display=swap" rel="stylesheet">
<style>
  :root {
    --stage: #e6e8eb;
    --brand-blue: #1a86bf;
    --brand-blue-deep: #0f6fa3;
    --brand-navy: #173f6e;
    --card-white: #fbfbfc;
    --ink: #2a2a2a;
    --tagline: #5a9fc7;
  }
  * { box-sizing: border-box; margin: 0; padding: 0; }
  html, body { width: 1200px; height: 873px; overflow: hidden; }
  body {
    background: var(--stage);
    font-family: "Open Sans", Arial, sans-serif;
    position: relative;
  }
  .card {
    position: absolute;
    top: 288px;
    width: 520px;
    height: 297px;
    border-radius: 18px;
    box-shadow: 0 10px 28px rgba(0,0,0,.18);
    overflow: hidden;
  }
  /* Front side */
  .card-front {
    left: 50px;
    background: linear-gradient(160deg, var(--brand-blue) 0%, var(--brand-blue-deep) 100%);
    color: #fff;
  }
  .front-lockup {
    position: absolute;
    left: 32px;
    bottom: 34px;
  }
  .front-name {
    font-size: 30px;
    font-weight: 700;
    letter-spacing: .5px;
    text-transform: uppercase;
    line-height: 1.05;
  }
  .front-tagline {
    margin-top: 6px;
    font-size: 13px;
    font-weight: 400;
    color: #e3f1f9;
  }
  /* Back side */
  .card-back {
    left: 630px;
    background: var(--card-white);
    color: var(--ink);
  }
  .brand {
    position: absolute;
    left: 26px;
    top: 30px;
    display: flex;
    align-items: center;
    gap: 12px;
  }
  .brand-dot {
    width: 46px;
    height: 46px;
    border-radius: 50%;
    background: var(--brand-blue);
  }
  .brand-name {
    font-size: 22px;
    font-weight: 700;
    color: var(--brand-navy);
    text-transform: uppercase;
    line-height: 1.05;
  }
  .brand-tagline {
    font-size: 11px;
    color: var(--tagline);
    margin-top: 2px;
  }
  .person {
    position: absolute;
    right: 26px;
    top: 98px;
    text-align: right;
  }
  .person-name {
    font-size: 18px;
    color: var(--brand-blue);
    font-weight: 400;
    padding-bottom: 2px;
  }
  .person-name strong { font-weight: 700; }
  .person-title {
    font-size: 10px;
    font-weight: 600;
    color: var(--ink);
    margin-top: 3px;
  }
  .divider {
    position: absolute;
    left: 26px;
    right: 26px;
    top: 150px;
    height: 2px;
    background: var(--brand-blue);
  }
  .address {
    position: absolute;
    right: 26px;
    top: 162px;
    text-align: right;
    font-size: 14px;
    font-style: normal;
    font-weight: 700;
    color: var(--brand-blue);
    line-height: 1.45;
  }
  .contacts {
    position: absolute;
    left: 26px;
    bottom: 24px;
    list-style: none;
  }
  .contacts li {
    display: flex;
    align-items: center;
    gap: 9px;
    font-size: 15px;
    font-weight: 600;
    color: var(--ink);
    height: 28px;
  }
  .contact-icon {
    width: 21px;
    height: 21px;
    flex: none;
  }
</style>
</head>
<body>
  <section class="card card-front" aria-label="Business card front">
    <div class="front-lockup">
      <p class="front-name">Clearpath Clinical</p>
      <p class="front-tagline">connected to your clinic</p>
    </div>
  </section>

  <section class="card card-back" aria-label="Business card back">
    <div class="brand">
      <span class="brand-dot"></span>
      <div>
        <p class="brand-name">Clearpath Clinical</p>
        <p class="brand-tagline">connected to your clinic</p>
      </div>
    </div>

    <div class="person">
      <p class="person-name">Warren <strong>Hale</strong></p>
      <p class="person-title">Athletic Director</p>
    </div>

    <div class="divider"></div>

    <address class="address">
      48 Alder Lane<br>
      Brookfield, OH 44403
    </address>

    <ul class="contacts">
      <li>
        <svg class="contact-icon" viewBox="0 0 22 22" aria-hidden="true">
          <circle cx="11" cy="11" r="11" fill="#1a86bf"/>
          <path d="M6 8.5c0-1 1-1.8 5-1.8s5 .8 5 1.8v1h-2.3V8.6h-5.4v.9H6z M7.5 11h7l1 4.5h-9z" fill="#fff"/>
        </svg>
        555-210-4410
      </li>
      <li>
        <svg class="contact-icon" viewBox="0 0 22 22" aria-hidden="true">
          <circle cx="11" cy="11" r="11" fill="#1a86bf"/>
          <rect x="7.5" y="5.5" width="7" height="3.5" fill="#fff"/>
          <rect x="5.5" y="9.5" width="11" height="5" rx="1" fill="#fff"/>
          <rect x="7.5" y="13" width="7" height="3.5" fill="#fff" stroke="#1a86bf" stroke-width=".8"/>
        </svg>
        555-210-4412
      </li>
      <li>
        <svg class="contact-icon" viewBox="0 0 22 22" aria-hidden="true">
          <circle cx="11" cy="11" r="11" fill="#1a86bf"/>
          <rect x="5.5" y="7" width="11" height="8" fill="#fff"/>
          <path d="M5.5 7l5.5 4.5L16.5 7" fill="none" stroke="#1a86bf" stroke-width="1.1"/>
        </svg>
        hello@clearpathclinical.com
      </li>
    </ul>
  </section>
</body>
</html>
```